弊社で製造・販売しているお酢のラベルデザインをお願いします。

商品は純りんご酢にはちみつを合わせた物で、4倍程度に希釈して健康飲料として利用してもらう物です。(料理にも使えます)

以前よりこの商品は500ml入りとして販売していましたが、昨今の原料費高騰等を受け、
容量を300mlに変更する事にしました。
瓶も、角瓶だったものを丸瓶に変更します。
ご愛顧いただいていたお客様に、なるべく「これまでのがすごく小さく(少なく)なってしまった・・・」という印象をもたれないように、全く新しいイメージのラベルデザインにしたいと考えています。

価格は1300円程度です。
お酢としては高額の商品ですので、「高級感」のあるデザインを希望します。

さらに、購入者のほとんどが女性ですので、女性が手に取りたくなるような
「かわいらしさ」あるいは「オシャレ感」、「健康」をイメージさせるデザインを希望します。

もちろん、スーパーや百貨店の売り場に並んだ際、他社の商品に埋もれない
目を引くデザインであってほしいと思います。

ラベルサイズは縦90mm×横145mm
瓶に巻いた際に正面に見える部分は、おおよそ90mm×73mm になります。

商品名は「朝つゆ果房のしらべ」
商品名以外に正面に見える部分に入れてほしい文言は以下の3つです。

「4倍濃縮タイプ」「国内産りんご果汁使用」「あなたの元気を応援!」

写真ファイルを添付しますが、
新しい瓶は丸型で色は緑。キャップはゴールドです。

これまでの商品写真も添付致します。
イメージの全く違うものを希望します。

今回は、既存の商品の容量を小さくするにあたり、これまでとは違う雰囲気である事を最大のポイントとしました。

当選ラベルは、これまでの「かわいらしい」イメージから、大人っぽさ、清楚で上品な雰囲気を感じさせ好感を得ました。
またりんご型の白地に商品名が映え、目を引きました。白地の面積は修正により、正面からりんご型がより見えるようにしました。
ピンクのバックは赤やゴールド系のデザインが多かった中で、一際優しさを感じさせ、
女性が手に取りたくなる商品だと思います。

以上の理由により選ばせていただきました。

この度は、弊社商品のラベルデザインに多くの提案をいただき、ありがとうございました。

「りんご」と「はちみつ」という、よくある組み合わせでしたが、
どのデザインもそれぞれによく練られており選定には大変時間を要しました。

今回はご縁がなかった皆様におかれましても、
またの機会がありましたら、是非もう一度お力をお貸しいただければと思います。
本来であればお一人お一人にお礼を申し上げるべきですのに、
このコメントをもってお礼に代えさせていただきます事、どうぞご容赦ください。

ご応募、本当にありがとうございました。

```html
<!DOCTYPE html>
<html lang="ja">
<head>
<meta charset="utf-8">
<title>朝つゆ果房のしらべ ラベルデザイン</title>
<link href="https://fonts.googleapis.com/css2?family=Noto+Serif+JP:wght@300;400;500&family=Cormorant+Garamond:wght@400;500&family=Montserrat:wght@300;400&display=swap" rel="stylesheet">
<style>
  :root {
    --paper: #ffffff;
    --ink: #4a4a4a;
    --ink-soft: #8a8a8a;
    --line: #c9c4c0;
    --accent: #e79aa6;
    --apple-light: #f7eeee;
    --apple-mid: #eedfe0;
    --bottle-dark: #8fa34a;
    --bottle-light: #dfe8b8;
    --swatch: #efefef;
  }
  html, body { margin: 0; padding: 0; }
  body {
    width: 846px; height: 1200px; overflow: hidden;
    background: var(--paper); color: var(--ink);
    font-family: "Noto Serif JP", serif; position: relative;
  }
  .sheet-title {
    position: absolute; left: 26px; top: 14px;
    font-family: "Montserrat", sans-serif; font-weight: 300;
    font-size: 13px; letter-spacing: 0.14em; line-height: 1.3; color: var(--ink);
  }
  .sheet-title .number { font-size: 22px; letter-spacing: 0.08em; }
  .dimension {
    position: absolute; left: 333px; width: 287px; height: 12px;
    border-left: 1px solid var(--accent); border-right: 1px solid var(--accent);
  }
  .dimension::before {
    content: ""; position: absolute; left: 0; right: 0; top: 6px;
    border-top: 1px solid var(--accent);
  }
  .dimension span {
    position: absolute; left: 50%; top: -2px; transform: translateX(-50%);
    background: var(--paper); padding: 0 6px;
    font-family: "Montserrat", sans-serif; font-size: 9px; color: var(--accent);
  }
  .dimension.top { top: 108px; }
  .dimension.bottom { top: 556px; }
  .front-guide {
    position: absolute; top: 127px; height: 423px; left: 333px; width: 287px;
    border-left: 1px dashed #f2c4cb; border-right: 1px dashed #f2c4cb;
  }
  .label {
    position: absolute; left: 141px; top: 127px; width: 677px; height: 423px;
    border: 1px solid var(--line); box-sizing: border-box; background: var(--paper);
  }
  .size-note {
    position: absolute; left: 60px; top: 578px;
    font-family: "Montserrat", sans-serif; font-size: 10px; color: var(--ink);
  }
  .nutrition {
    position: absolute; font-size: 7.5px; line-height: 1.55; color: var(--ink);
    border-collapse: collapse;
  }
  .nutrition caption { text-align: left; font-size: 7.5px; padding-bottom: 2px; }
  .nutrition td { padding: 0 12px 0 0; }
  .nutrition.upper { left: 14px; top: 14px; }
  .nutrition.lower { left: 14px; top: 240px; }
  .nutrition.lower td { border-bottom: 1px solid var(--line); }
  .ingredients {
    position: absolute; left: 498px; top: 16px; width: 160px;
    font-size: 7.5px; line-height: 1.6; color: var(--ink);
  }
  .ingredients p { margin: 0; }
  .apple-mark { position: absolute; left: 194px; top: 80px; }
  .cheer {
    position: absolute; left: 339px; top: 96px; transform: translateX(-50%);
    font-size: 9px; letter-spacing: 0.15em; white-space: nowrap;
  }
  .product-name {
    position: absolute; left: 339px; top: 178px; transform: translateX(-50%);
    text-align: center; font-weight: 500; font-size: 27px; line-height: 1.45;
    letter-spacing: 0.12em; white-space: nowrap; color: var(--ink);
  }
  .product-name .sub { font-size: 16px; letter-spacing: 0.2em; }
  .english-name {
    position: absolute; left: 339px; top: 374px; transform: translateX(-50%);
    font-family: "Cormorant Garamond", serif; font-size: 12px;
    letter-spacing: 0.12em; white-space: nowrap;
  }
  .label-footer {
    position: absolute; left: 339px; top: 396px; transform: translateX(-50%);
    font-size: 7px; letter-spacing: 0.1em; white-space: nowrap; color: var(--ink-soft);
  }
  .label-footer span + span { margin-left: 26px; }
  .package-title {
    position: absolute; left: 268px; top: 570px;
    font-family: "Montserrat", sans-serif; font-size: 10px;
    letter-spacing: 0.14em; line-height: 1.4;
  }
  .bottle-photo { position: absolute; left: 325px; top: 610px; }
  .leader { position: absolute; left: 500px; top: 760px; }
  .concept {
    position: absolute; left: 612px; top: 760px; width: 130px;
    font-size: 10.5px; line-height: 2; letter-spacing: 0.06em; color: var(--ink);
  }
  .concept p { margin: 0; }
  .swatch {
    position: absolute; left: 652px; top: 960px; width: 180px; height: 225px;
    background: var(--swatch);
  }
</style>
</head>
<body>
  <div class="sheet-title">LABEL<br>DESIGN <span class="number">01</span></div>

  <div class="dimension top"><span>W73mm</span></div>
  <section class="label" aria-label="ラベル展開図">
    <table class="nutrition upper">
      <caption>栄養成分表示（100ml当り）</caption>
      <tr><td>エネルギー</td><td>96kcal</td></tr>
      <tr><td>たんぱく質</td><td>0g</td></tr>
      <tr><td>脂質</td><td>0g</td></tr>
      <tr><td>炭水化物</td><td>24g</td></tr>
      <tr><td>食塩相当量</td><td>0g</td></tr>
    </table>

    <div class="ingredients">
      <p>お召し上がり方</p>
      <p>水や炭酸水で約4倍に薄めて</p>
      <p>お召し上がりください。</p>
      <p>開栓後は冷蔵庫で保存し、</p>
      <p>お早めにお使いください。</p>
    </div>

    <svg class="apple-mark" width="290" height="290" viewBox="0 0 290 290" role="img" aria-label="りんご型の線画と中央の白い銘板">
      <defs>
        <radialGradient id="appleTone" cx="50%" cy="55%" r="55%">
          <stop offset="0%" stop-color="var(--apple-light)"/>
          <stop offset="100%" stop-color="var(--apple-mid)"/>
        </radialGradient>
      </defs>
      <ellipse cx="145" cy="160" rx="128" ry="120" fill="url(#appleTone)"/>
      <ellipse cx="145" cy="160" rx="80" ry="92" fill="var(--paper)"/>
    </svg>

    <div class="cheer">あなたの元気を応援</div>
    <h1 class="product-name">朝つゆ果房<br><span class="sub">のしらべ</span></h1>
    <div class="english-name">APPLE VINEGAR AND HONEY</div>
    <div class="label-footer"><span>国内産りんご果汁使用</span><span>4倍濃縮タイプ</span></div>

    <table class="nutrition lower">
      <caption>栄養成分表示（希釈後200ml当り）</caption>
      <tr><td>熱量</td><td>48kcal</td></tr>
      <tr><td>たんぱく質</td><td>0.0g</td></tr>
      <tr><td>脂質</td><td>0.0g</td></tr>
      <tr><td>炭水化物</td><td>12.0g</td></tr>
      <tr><td>食塩相当量</td><td>0.0g</td></tr>
    </table>
  </section>
  <div class="front-guide" aria-hidden="true"></div>
  <div class="dimension bottom"><span>W73mm</span></div>
  <div class="size-note">W145mm x H90mm</div>

  <div class="package-title">PACKAGE<br>IMAGE</div>
  <svg class="bottle-photo" width="240" height="580" viewBox="0 0 240 580" role="img" aria-label="緑の丸瓶にゴールドのキャップ、白いラベルを巻いた商品写真">
    <defs>
      <linearGradient id="glass" x1="0" x2="1">
        <stop offset="0%" stop-color="var(--bottle-dark)"/>
        <stop offset="45%" stop-color="var(--bottle-light)"/>
        <stop offset="100%" stop-color="var(--bottle-dark)"/>
      </linearGradient>
    </defs>
    <rect x="0" y="0" width="240" height="580" fill="url(#glass)" opacity="0.9"/>
  </svg>
  <svg class="leader" width="110" height="40" viewBox="0 0 110 40" aria-hidden="true">
    <line x1="0" y1="36" x2="104" y2="4" stroke="var(--ink)" stroke-width="0.8"/>
  </svg>
  <div class="concept">
    <p>自然の素材や</p>
    <p>製法のこだわりを</p>
    <p>感じさせる</p>
    <p>清楚感のある</p>
    <p>柔らかなイメージの</p>
    <p>容器を目指しました。</p>
  </div>
  <div class="swatch" aria-hidden="true"></div>
</body>
</html>
```